Banner 34"x81"

This is for a Pull Up Banner
I am supplying a sample of my logo and some of my art work for you to incorporate into an upright banner.
Please business name:TessaLo QuietHarbor Psychotherapy
phone number: 905-318-4470 NOT THE ONE ON THE BUSINESS CARD

```html
<!DOCTYPE html>
<html lang="en">
<head>
<meta charset="utf-8">
<title>Tessa Lo – QuietHarbor Psychotherapy Pull Up Banner</title>
<link href="https://fonts.googleapis.com/css2?family=Lato:wght@300;400;700;900&display=swap" rel="stylesheet">
<style>
  :root {
    --navy: #233a8c;
    --logo-blue: #2258a8;
    --photo-dark: #25283d;
    --photo-blue: #2a55c8;
    --gold: #f2c55a;
    --gold-deep: #d8a540;
    --band-black: #161616;
    --white: #ffffff;
    --soft-white: #cfd7f0;
  }
  * { margin: 0; padding: 0; box-sizing: border-box; }
  html, body {
    width: 1200px;
    height: 2733px;
    overflow: hidden;
    background: var(--navy);
  }
  .banner {
    position: relative;
    width: 1200px;
    height: 2733px;
    overflow: hidden;
    background: var(--navy);
    font-family: "Lato", sans-serif;
    color: var(--gold);
  }
  .texture-area {
    position: absolute;
    background: linear-gradient(135deg, var(--gold) 0%, var(--gold-deep) 100%);
  }
  .texture-area--top {
    left: 0; top: 0;
    width: 410px; height: 390px;
  }
  .texture-area--bottom {
    left: 660px; top: 2465px;
    width: 540px; height: 268px;
  }
  .portrait {
    position: absolute;
    left: 270px; top: 95px;
    width: 870px; height: 1235px;
    background: linear-gradient(180deg, var(--photo-dark) 0%, var(--photo-dark) 30%, var(--photo-blue) 55%, var(--photo-blue) 100%);
  }
  .divider-rule {
    position: absolute;
    left: 0; top: 1330px;
    width: 1200px; height: 14px;
    background: var(--gold);
  }
  .logo-mark {
    position: absolute;
    left: 405px; top: 1412px;
    width: 390px; height: 310px;
    background: var(--logo-blue);
    display: flex;
    align-items: center;
    justify-content: center;
    color: var(--white);
    font-weight: 700;
    font-size: 76px;
  }
  .identity {
    position: absolute;
    left: 0; top: 1790px;
    width: 1200px;
    text-align: center;
  }
  .identity__name {
    font-weight: 900;
    font-size: 96px;
    line-height: 1.1;
    color: var(--gold);
  }
  .identity__practice {
    font-weight: 400;
    font-size: 64px;
    line-height: 1.2;
    margin-top: 6px;
    color: var(--gold);
  }
  .identity__email {
    font-weight: 300;
    font-size: 40px;
    margin-top: 14px;
    color: var(--soft-white);
  }
  .phone-band {
    position: absolute;
    left: 0; top: 2157px;
    width: 1200px; height: 128px;
    background: var(--band-black);
    border-top: 5px solid var(--gold);
    border-bottom: 5px solid var(--gold);
    display: flex;
    align-items: center;
    justify-content: center;
  }
  .phone-band__number {
    font-weight: 900;
    font-size: 102px;
    line-height: 1;
    color: var(--gold);
    letter-spacing: 1px;
  }
  .social {
    position: absolute;
    left: 0; top: 2310px;
    width: 1200px;
    display: flex;
  }
  .social__item {
    flex: 1;
    display: flex;
    flex-direction: column;
    align-items: center;
    padding-top: 10px;
  }
  .social__item + .social__item { border-left: 3px solid var(--soft-white); }
  .social__badge {
    width: 64px; height: 64px;
    border: 3px solid var(--white);
    border-radius: 8px;
    background: var(--logo-blue);
  }
  .social__handle {
    margin-top: 12px;
    font-size: 40px;
    font-weight: 400;
    color: var(--white);
  }
</style>
</head>
<body>
<main class="banner">
  <div class="texture-area texture-area--top" role="img" aria-label="Gold foil texture area"></div>

  <div class="portrait" role="img" aria-label="Portrait photo of Tessa Lo in a blue sweater"></div>
  <div class="divider-rule"></div>

  <div class="logo-mark">Tessa Lo</div>

  <section class="identity">
    <h1 class="identity__name">Tessa Lo</h1>
    <p class="identity__practice">QuietHarbor Psychotherapy</p>
    <p class="identity__email">TessaQuietHarbor@harbormail.ca</p>
  </section>

  <div class="phone-band">
    <span class="phone-band__number">905-318-4470</span>
  </div>

  <section class="social">
    <div class="social__item">
      <span class="social__badge"></span>
      <span class="social__handle">@TessaQuietHarbour</span>
    </div>
    <div class="social__item">
      <span class="social__badge"></span>
      <span class="social__handle">@TessaQuiet</span>
    </div>
  </section>

  <div class="texture-area texture-area--bottom" role="img" aria-label="Gold foil texture area"></div>
</main>
</body>
</html>
```